Eye-catching Yellow Page Ad for Attorney's Office

We need a phone book advertisement for our law office. We practice workers' compensation law, and our clientele consists exclusively of individuals who have been injured on the job. The dimensions of the print ad will be 6" W X 4.54" H.

We've had our current ad for several years, and wanted to get a new one that has been designed by a professional. Being that it's an ad for a law firm, it needs to be professional looking, but we're hoping to have something that looks a little more modern and has eye-catching appeal. We like the text that is included in the ad, and we want to make sure our phone number is very visible. No real preference for color scheme.

I've attached a copy of our current ad. All the information included in there is accurate. Our office name is Thornbury & Lisle, PLLC. The ethical rules for attorney advertising require the PLLC to be included in the ad, but it can be smaller than the other text (see our current ad).

Target Market(s)

Our potential clients are injured workers looking for legal representation in their workers' compensation claim.

Industry/Entity Type

Attorney

Font styles to use
Serif
Sans Serif

Requirements
Must have
• Professional, but stands out from the crowd
Nice to have
• Clean modern design
Should not have
• We don't want it to be too crowded or over-worked.

```html
<!DOCTYPE html>
<html lang="en">
<head>
<meta charset="utf-8">
<title>Thornbury &amp; Lisle, PLLC — Workers' Compensation</title>
<link rel="stylesheet" href="https://fonts.googleapis.com/css2?family=Jost:ital,wght@0,500;0,600;1,400&family=Oswald:wght@300;400&display=swap">
<style>
  :root {
    --cyan: #00adee;
    --ink: #060606;
    --paper: #ffffff;
    --white: #ffffff;
  }
  html, body { margin: 0; padding: 0; overflow: hidden; background: var(--paper); }
  .ad {
    position: relative;
    width: 1200px;
    height: 908px;
    background: var(--paper);
    overflow: hidden;
  }
  .firm-name {
    position: absolute;
    top: 4px; left: 0; width: 1200px;
    text-align: center;
    margin: 0;
    font-family: 'Jost', sans-serif;
    font-weight: 600;
    font-size: 104px;
    line-height: 1.2;
    color: var(--cyan);
    letter-spacing: 1px;
  }
  .firm-suffix {
    position: absolute;
    top: 30px; right: 50px;
    font-family: 'Jost', sans-serif;
    font-weight: 500;
    font-size: 21px;
    color: var(--cyan);
  }
  .panel {
    position: absolute;
    left: 29px; top: 131px;
    width: 1142px; height: 749px;
    background: var(--ink);
    color: var(--white);
    text-align: center;
  }
  .panel > * { position: absolute; left: 0; width: 100%; margin: 0; }
  .practice {
    top: 30px;
    font-family: 'Oswald', sans-serif;
    font-weight: 400;
    font-size: 68px;
    line-height: 1;
    letter-spacing: 1px;
  }
  .credential {
    top: 122px;
    font-family: 'Jost', sans-serif;
    font-style: italic;
    font-weight: 400;
    font-size: 27px;
    letter-spacing: 0.5px;
  }
  .promise {
    top: 172px;
    font-family: 'Oswald', sans-serif;
    font-weight: 300;
    font-size: 21px;
    line-height: 35px;
  }
  .values {
    top: 278px;
    font-family: 'Jost', sans-serif;
    font-weight: 600;
    font-size: 37px;
    color: var(--cyan);
    letter-spacing: 1.5px;
  }
  .help-intro {
    top: 355px;
    font-family: 'Jost', sans-serif;
    font-style: italic;
    font-weight: 400;
    font-size: 27px;
    letter-spacing: 1px;
  }
  .services {
    top: 400px;
    font-family: 'Oswald', sans-serif;
    font-weight: 300;
    font-size: 27px;
    line-height: 42px;
    padding: 0; list-style: none;
  }
  .services .sep {
    display: inline-block;
    width: 1px; height: 16px;
    background: var(--white);
    margin: 0 10px;
    vertical-align: middle;
  }
  .phone {
    top: 500px;
    font-family: 'Jost', sans-serif;
    font-weight: 600;
    color: var(--cyan);
    line-height: 1;
  }
  .phone .area { font-size: 88px; margin-right: 22px; }
  .phone .number { font-size: 132px; letter-spacing: 2px; }
  .address {
    top: 656px;
    font-family: 'Oswald', sans-serif;
    font-weight: 400;
    font-size: 22px;
  }
  .web {
    top: 690px;
    font-family: 'Jost', sans-serif;
    font-weight: 500;
    font-size: 30px;
    letter-spacing: 1.5px;
  }
</style>
</head>
<body>
<div class="ad">
  <h1 class="firm-name">Thornbury &amp; Lisle</h1>
  <span class="firm-suffix">PLLC</span>

  <section class="panel">
    <h2 class="practice">WORKERS’ COMPENSATION</h2>
    <p class="credential">Former Assistant Attorneys General Who Know The System</p>
    <p class="promise">At Thornbury &amp; Lisle, we provide personal attention to our clients.<br>That means your case is handled by an Attorney, not an assistant.</p>
    <p class="values">PROFESSIONAL • COMMITTED • EFFECTIVE</p>
    <p class="help-intro">We can help with:</p>
    <p class="services">
      Workplace Injuries Or Death<span class="sep"></span>Lost Wages<span class="sep"></span>Medical Expenses &amp; Treatment<br>
      Hearing Loss Claims<span class="sep"></span>Disability Awards<span class="sep"></span>Return To Work Issues
    </p>
    <p class="phone"><span class="area">360</span><span class="number">555-0142</span></p>
    <p class="address">412 W. Laurel Suite 300, Clearbrook</p>
    <p class="web">www.thornburylisle.com</p>
  </section>
</div>
</body>
</html>
```